One Page Website for Personal Trainer in London

I have a logo and need a one page website designed around my branding. I am a freelance Personal Trainer based in London specialising in bodyweight training for men and women. I would like the site to be modern and clean but not overtly urban in design.
I need the following headings:
About Me
My Services
Events
Blog
I don't need them to be seperate pages but if they can link to further down the page that would be great.
Industry/Entity Type
Personal Trainer
Coding
Coded - Design and coding required
Number of Pages Required
1 page
Requirements
Must have
- I need the following headings:
- About Me
- My Services
- Events
- Blog
- mobile friendly formatting
- health and fitness related photography
- Colour scheme in keeping with my existing logo

```html
<!DOCTYPE html>
<html lang="en">
<head>
<meta charset="utf-8">
<title>Harper Vale Personal Training</title>
<link href="https://fonts.googleapis.com/css2?family=Poppins:wght@400;500;600;700&display=swap" rel="stylesheet">
<style>
:root{
  --orange:#f07f1a;
  --orange-dark:#d96c0c;
  --charcoal:#262320;
  --charcoal-2:#1d1b19;
  --ink:#1f1f1f;
  --muted:#555;
  --light:#f2f2f2;
  --white:#fff;
}
*{box-sizing:border-box;margin:0;padding:0}
html,body{width:1200px;height:4353px;overflow:hidden}
body{font-family:'Poppins',sans-serif;color:var(--ink);background:var(--white);position:relative}
section,header,footer{position:absolute;left:0;width:1200px;overflow:hidden}
.abs{position:absolute}
.fill{position:absolute;inset:0}
.section-title{font-weight:700;font-size:38px;text-align:center;letter-spacing:.5px}
.title-rule{width:90px;height:3px;background:var(--orange);margin:14px auto 0}
.btn{position:absolute;display:flex;align-items:center;justify-content:center;font-size:13px;font-weight:600;letter-spacing:1px;text-transform:uppercase}
.btn-solid{background:var(--orange);color:var(--white)}
.btn-line{border:2px solid var(--white);color:var(--white)}
.btn-line-orange{border:2px solid var(--orange);color:var(--orange)}
.dot{display:inline-block;width:14px;height:14px;border-radius:50%}

/* hero */
.hero{top:0;height:634px}
.hero-photo{background:linear-gradient(180deg,#b9c9d6 0%,#8fa2ae 45%,#6e767b 75%,#5b5f60 100%)}
.brand{left:140px;top:24px;text-align:center}
.brand-name{font-size:30px;font-weight:600;color:var(--orange);line-height:1}
.brand-sub{font-size:11px;font-weight:600;color:var(--orange);letter-spacing:3px;margin-top:8px}
.nav{left:448px;top:44px;display:flex;gap:30px;font-size:15px;color:#222}
.nav a{color:inherit;text-decoration:none}
.nav a.active{color:var(--orange);border-bottom:2px solid var(--orange);padding-bottom:4px}
.social{display:flex;gap:10px}
.hero-social{left:1020px;top:48px}
.hero-kicker{left:650px;top:240px;border:3px solid var(--orange);padding:8px 16px;font-size:22px;font-weight:700;color:var(--orange);letter-spacing:1px}
.hero-head{left:650px;top:300px;font-size:52px;font-weight:700;color:var(--white);letter-spacing:1px}
.hero-tab{left:584px;top:614px;width:32px;height:20px;background:var(--orange);border-radius:4px 4px 0 0}

/* audience */
.audience{top:634px;height:360px;background:var(--orange);color:var(--white)}
.aud-block{top:90px;width:300px}
.aud-block h3{font-size:36px;font-weight:700;line-height:1.2}
.aud-block p{font-size:13px;line-height:1.6;margin-top:8px}
.aud-men{left:165px;text-align:right}
.aud-women{left:755px}
.aud-photo{left:485px;top:50px;width:230px;height:310px;background:linear-gradient(180deg,#c2693a,#7a4a36 60%,#3a2f2c)}

/* about */
.about{top:994px;height:482px;background:var(--white)}
.about-photo{right:0;top:0;width:520px;height:482px;background:linear-gradient(90deg,rgba(255,255,255,1),rgba(226,226,226,.9))}
.about-left-photo{left:0;top:120px;width:280px;height:362px;background:linear-gradient(90deg,#e4e4e4,rgba(255,255,255,1))}
.about .section-title{position:absolute;top:60px;left:0;width:100%}
.about-col{top:150px;font-size:13px;line-height:1.65;color:var(--muted)}
.about-col.left{left:282px;width:350px;text-align:right}
.about-col.right{left:660px;width:300px}

/* services */
.services{top:1476px;height:602px;background:var(--charcoal);color:var(--white)}
.services .section-title{position:absolute;top:68px;width:100%}
.services-intro{top:150px;left:280px;width:640px;text-align:center;font-size:14px;line-height:1.6}
.svc{width:290px}
.svc h4{font-size:13px;font-weight:700;letter-spacing:.5px}
.svc p{font-size:12px;line-height:1.6;margin-top:4px;color:#e5e5e5}
.svc.l{left:240px;text-align:right}
.svc.r{left:705px}
.svc-icon{width:58px;height:58px;background:var(--orange);display:flex;align-items:center;justify-content:center}

/* events */
.events{top:2078px;height:668px;background:#ececec}
.events-photo{left:0;top:0;width:700px;height:668px;background:linear-gradient(90deg,#8a8c8e,#b7b9bb 55%,#e8e8e8)}
.events-title{left:585px;top:80px;font-size:38px;font-weight:700}
.events-rule{left:730px;top:132px;width:90px;height:3px;background:var(--orange)}
.calendar{left:465px;top:162px;width:616px;background:var(--white);box-shadow:0 4px 14px rgba(0,0,0,.15)}
.cal-head{height:46px;background:var(--orange);display:flex;align-items:center;padding-left:20px;color:var(--white);font-weight:700;font-size:18px;gap:10px}
.cal-arrows{display:flex;gap:2px}
.cal-arrows span{width:20px;height:20px;background:var(--white);opacity:.85}
.cal-strip{height:24px;background:var(--charcoal-2)}
.cal-grid{display:grid;grid-template-columns:repeat(7,1fr);gap:4px;padding:8px 6px;background:#e6e6e6}
.cal-grid div{height:46px;background:var(--light);display:flex;align-items:center;justify-content:center;font-size:14px;font-weight:600;color:#333}
.cal-grid .dow{height:26px;background:var(--orange);color:var(--white);font-size:12px;font-weight:700}
.cal-grid .o{color:var(--orange)}
.cal-grid .today{background:var(--orange);color:var(--white)}
.cal-grid .empty{background:var(--white)}
.cal-foot{height:40px;background:var(--charcoal-2);color:var(--white);display:flex;align-items:center;font-weight:700;font-size:15px}
.cal-foot b{width:40px;height:40px;background:var(--orange);display:flex;align-items:center;justify-content:center;margin-right:14px}

/* cta */
.cta{top:2746px;height:378px;background:linear-gradient(90deg,#e8781a,#f39a45 50%,#e8781a);color:var(--white);text-align:center}
.cta-kicker{top:130px;width:100%;font-size:22px;font-weight:500}
.cta-head{top:162px;width:100%;font-size:44px;font-weight:700;letter-spacing:1px}

/* blog */
.blog{top:3124px;height:625px;background:var(--white)}
.blog-title{left:155px;top:78px;font-size:34px;font-weight:700}
.blog-arrows{left:1010px;top:88px;display:flex;gap:6px}
.blog-arrows span{width:30px;height:30px;border:2px solid var(--orange);display:flex;align-items:center;justify-content:center}
.post{top:160px;width:270px}
.post-photo{height:160px;background:linear-gradient(135deg,#c9c4c8,#9a8f95 50%,#d6b8c4)}
.post.featured .post-photo{outline:6px solid var(--orange)}
.post h5{font-size:17px;font-weight:700;line-height:1.35;margin-top:26px}
.post p{font-size:13px;line-height:1.7;color:var(--muted);margin-top:12px}

/* contact */
.contact{top:3749px;height:604px;background:var(--charcoal);color:var(--white)}
.contact .section-title{position:absolute;top:62px;width:100%}
.field{position:absolute;border:2px solid #d8d8d8;height:38px;padding:8px 12px;font-size:14px;color:#ddd}
.field.msg{height:120px}
.contact-info{left:195px;font-size:13px;display:flex;align-items:center;gap:10px}
.footer-rule{left:195px;top:494px;width:810px;height:1px;background:#666}
.copyright{top:520px;width:100%;text-align:center;font-size:14px;color:#ddd}
.footer-social{left:955px;top:522px}
</style>
</head>
<body>

<header class="hero">
  <div class="fill hero-photo" role="img" aria-label="Photo of a woman running across a London bridge with a red bus and the clock tower behind"></div>
  <div class="abs brand"><div class="brand-name">Harper Vale</div><div class="brand-sub">PERSONAL TRAINING</div></div>
  <nav class="abs nav">
    <a class="active" href="#home">Home</a><a href="#about">About Me</a><a href="#services">My Services</a><a href="#events">Events</a><a href="#blog">Blog</a><a href="#contact">Contact Me</a>
  </nav>
  <div class="abs social hero-social"><span class="dot" style="background:#333"></span><span class="dot" style="background:#333"></span><span class="dot" style="background:#333"></span><span class="dot" style="background:#333"></span></div>
  <div class="abs hero-kicker">GET IN TO SHAPE</div>
  <div class="abs hero-head">AND BE HAPPY</div>
  <div class="btn btn-solid" style="left:650px;top:375px;width:160px;height:44px">Learn more</div>
  <div class="abs hero-tab"></div>
</header>

<section class="audience">
  <div class="abs aud-block aud-men">
    <h3>FOR MEN</h3>
    <p>Lorem ipsum dolor sit amet, conse ctetur adi sollicitudin. Suspendisse pulvinar, velit nec pharetra interdum, ante tellus ornare mi, et mollis tellus neque vitae elit.</p>
  </div>
  <div class="btn btn-line" style="left:345px;top:300px;width:118px;height:40px;font-size:11px">Get started</div>
  <div class="abs aud-photo" role="img" aria-label="Photo of a man with dumbbells and a woman in sportswear"></div>
  <div class="abs aud-block aud-women">
    <h3>FOR WOMEN</h3>
    <p>Lorem ipsum dolor sit amet, conse ctetur adi sollicitudin. Suspendisse pulvinar, velit nec pharetra interdum, ante tellus ornare mi, et mollis tellus neque vitae elit.</p>
  </div>
  <div class="btn btn-line" style="left:757px;top:300px;width:118px;height:40px;font-size:11px">Get started</div>
</section>

<section class="about" id="about">
  <div class="abs about-left-photo" role="img" aria-label="Faded photo of gym equipment"></div>
  <div class="abs about-photo" role="img" aria-label="Faded photo of a gym interior"></div>
  <h2 class="section-title">ABOUT ME</h2>
  <div class="title-rule" style="position:absolute;top:116px;left:555px;margin:0"></div>
  <p class="abs about-col left">Lorem ipsum dolor sit amet, consectetur adipiscing elit. Curabitur sed purus quam. Vestibulum lobortis consequat mauris id fringilla. Morbi eros purus, commodo non tortor ut, tempus ornare est. Suspendisse suscipit nec metus non pellentesque. Morbi at enim nisl. Phasellus sed condimentum enim, non viverra eros.</p>
  <p class="abs about-col right">Quisque commodo erat vel sapien suscipit accumsan. Fusce eu eleifend mi. Integer hendrerit, dolor non sagittis consequat, enim ex gravida lacus, quis dignissim augue urna non mauris. Nullam eros massa, fringilla sit amet leo quis, tincidunt lobortis leo. Praesent imperdiet sapien dapibus, hendrerit nisi ac, aliquet diam.</p>
  <div class="btn btn-line-orange" style="left:530px;top:365px;width:140px;height:38px;font-size:11px">Contact me</div>
</section>

<section class="services" id="services">
  <h2 class="section-title">MY SERVICES</h2>
  <div class="title-rule" style="position:absolute;top:122px;left:555px;margin:0"></div>
  <p class="abs services-intro">Lorem ipsum dolor sit amet, consectetur adipiscing elit. Curabitur sed purus quam. Vestibulum lobortis consequat mauris id fringilla. Morbi eros purus, commodo non.</p>

  <div class="abs svc l" style="top:240px"><h4>WEIGHT LOSS</h4><p>Lorem ipsum dolor sit amet, consectetur adipiscing elit. Curabitur sed purus.</p></div>
  <div class="abs svc-icon" style="left:540px;top:238px"><svg width="30" height="30" viewBox="0 0 30 30" fill="none" stroke="#fff" stroke-width="2.5"><rect x="4" y="6" width="22" height="18" rx="2"/><path d="M9 14a6 6 0 0 1 12 0M15 14l3-3"/></svg></div>
  <div class="abs svc-icon" style="left:625px;top:238px"><svg width="30" height="30" viewBox="0 0 30 30" fill="none" stroke="#fff" stroke-width="2.5"><circle cx="15" cy="7" r="3"/><path d="M8 14h14M15 10v10M10 27l5-7 5 7"/></svg></div>
  <div class="abs svc r" style="top:240px"><h4>BODY BUILDING</h4><p>Lorem ipsum dolor sit amet, consectetur adipiscing elit. Curabitur sed purus.</p></div>

  <div class="abs svc l" style="top:335px"><h4>WEIGHT LIFTING</h4><p>Lorem ipsum dolor sit amet, consectetur adipiscing elit. Curabitur sed purus.</p></div>
  <div class="abs svc-icon" style="left:540px;top:333px"><svg width="32" height="20" viewBox="0 0 32 20" fill="#fff"><rect x="1" y="5" width="4" height="10"/><rect x="6" y="2" width="4" height="16"/><rect x="10" y="8" width="12" height="4"/><rect x="22" y="2" width="4" height="16"/><rect x="27" y="5" width="4" height="10"/></svg></div>
  <div class="abs svc-icon" style="left:625px;top:333px"><svg width="32" height="30" viewBox="0 0 32 30" fill="none" stroke="#fff" stroke-width="2.5"><circle cx="7" cy="23" r="5"/><circle cx="25" cy="23" r="5"/><path d="M7 23l7-10h8l3 10M14 13l-2-5h-3"/><circle cx="20" cy="5" r="2.5" fill="#fff"/></svg></div>
  <div class="abs svc r" style="top:335px"><h4>INDOOR CYCLING</h4><p>Lorem ipsum dolor sit amet, consectetur adipiscing elit. Curabitur sed purus.</p></div>

  <div class="abs svc l" style="top:430px"><h4>BOXING FOR GIRLS</h4><p>Lorem ipsum dolor sit amet, consectetur adipiscing elit. Curabitur sed purus.</p></div>
  <div class="abs svc-icon" style="left:540px;top:428px"><svg width="30" height="30" viewBox="0 0 30 30" fill="none" stroke="#fff" stroke-width="2.5"><circle cx="15" cy="5" r="3"/><path d="M15 9v10M8 12l7 2 7-5M15 19l-5 9M15 19l5 9"/></svg></div>
  <div class="abs svc-icon" style="left:625px;top:428px"><svg width="30" height="30" viewBox="0 0 30 30" fill="none" stroke="#fff" stroke-width="2.5"><circle cx="20" cy="5" r="3"/><path d="M18 10l-6 8 -6 2M18 10l4 7 6 1M12 18l4 10"/></svg></div>
  <div class="abs svc r" style="top:430px"><h4 style="font-weight:500">PSYCHOLOGY TRAINING</h4><p>Lorem ipsum dolor sit amet, consectetur adipiscing elit. Curabitur sed purus.</p></div>
</section>

<section class="events" id="events">
  <div class="abs events-photo" role="img" aria-label="Photo of a man stretching in a gym"></div>
  <h2 class="abs events-title">MY EVENT CALENDAR</h2>
  <div class="abs events-rule"></div>
  <div class="abs calendar">
    <div class="cal-head">OCTOBER, 2017 <span class="cal-arrows"><span></span><span></span></span></div>
    <div class="cal-strip"></div>
    <div class="cal-grid">
      <div class="dow">MON</div><div class="dow">TUE</div><div class="dow">WED</div><div class="dow">THU</div><div class="dow">FRI</div><div class="dow">SAT</div><div class="dow">SUN</div>
      <div>-</div><div>-</div><div>-</div><div>-</div><div>-</div><div>-</div><div class="o">1</div>
      <div>2</div><div class="o">3</div><div>4</div><div>5</div><div class="o">6</div><div>7</div><div class="o">8</div>
      <div>9</div><div class="o">10</div><div>11</div><div>12</div><div class="o">13</div><div class="o">14</div><div class="o">15</div>
      <div>16</div><div class="o">17</div><div>18</div><div>19</div><div class="today">20</div><div class="o">21</div><div class="o">22</div>
      <div>23</div><div class="o">24</div><div>25</div><div>26</div><div class="o">27</div><div class="o">28</div><div class="o">29</div>
      <div>30</div><div class="o">31</div><div class="empty"></div><div class="empty"></div><div class="empty"></div><div class="empty"></div><div class="empty"></div>
    </div>
    <div class="cal-foot"><b>20</b>WEIGHT LOSS</div>
  </div>
</section>

<section class="cta">
  <div class="fill" role="img" aria-label="Orange-toned photo of a group fitness class" style="background:linear-gradient(180deg,rgba(0,0,0,.05),rgba(0,0,0,.12))"></div>
  <div class="abs cta-kicker">START YOUR</div>
  <div class="abs cta-head">TRAINING TODAY</div>
  <div class="btn btn-line" style="left:530px;top:235px;width:140px;height:40px;font-size:11px">Contact me</div>
</section>

<section class="blog" id="blog">
  <h2 class="abs blog-title">LATEST BLOG</h2>
  <div class="abs blog-arrows">
    <span><svg width="10" height="12" viewBox="0 0 10 12"><path d="M8 1L2 6l6 5" fill="none" stroke="#f07f1a" stroke-width="2"/></svg></span>
    <span style="background:var(--orange)"><svg width="10" height="12" viewBox="0 0 10 12"><path d="M2 1l6 5-6 5" fill="none" stroke="#fff" stroke-width="2"/></svg></span>
  </div>
  <article class="abs post" style="left:157px">
    <div class="post-photo" role="img" aria-label="Photo of a woman lifting dumbbells"></div>
    <h5>Lorem ipsum dolor sit amet, consectetur adipiscing.</h5>
    <p>Vestibulum lobortis consequat mauris id fringilla. Morbi eros purus, commodo non tortor ut, tempus ornare...</p>
  </article>
  <article class="abs post featured" style="left:465px">
    <div class="post-photo" role="img" aria-label="Photo of a woman training on a treadmill"></div>
    <h5>Lorem ipsum dolor sit amet, consectetur adipiscing.</h5>
    <p>Vestibulum lobortis consequat mauris id fringilla. Morbi eros purus, commodo non tortor ut, tempus ornare...</p>
  </article>
  <article class="abs post" style="left:775px">
    <div class="post-photo" role="img" aria-label="Photo of a women's fitness class"></div>
    <h5>Lorem ipsum dolor sit amet, consectetur adipiscing.</h5>
    <p>Vestibulum lobortis consequat mauris id fringilla. Morbi eros purus, commodo non tortor ut, tempus ornare...</p>
  </article>
  <div class="btn btn-solid" style="left:533px;top:502px;width:134px;height:44px;text-transform:none;font-weight:500;font-size:14px">Read All&nbsp;<svg width="14" height="12" viewBox="0 0 14 12"><path d="M1 6l12-5-4 11-2-5z" fill="#fff"/></svg></div>
</section>

<footer class="contact" id="contact">
  <h2 class="section-title">CONTACT ME</h2>
  <div class="title-rule" style="position:absolute;top:118px;left:555px;margin:0"></div>
  <div class="field" style="left:195px;top:156px;width:385px">Name</div>
  <div class="field" style="left:612px;top:156px;width:393px">Email</div>
  <div class="field" style="left:195px;top:206px;width:385px">Phone No.</div>
  <div class="field" style="left:612px;top:206px;width:393px">Subject</div>
  <div class="field msg" style="left:195px;top:260px;width:810px">Message</div>
  <div class="abs contact-info" style="top:405px"><svg width="14" height="14" viewBox="0 0 14 14"><path d="M3 1l3 3-2 2c1 2 2 3 4 4l2-2 3 3-2 2C6 13 1 8 1 3z" fill="#fff"/></svg><b>(020) 555-0147</b></div>
  <div class="abs contact-info" style="top:432px"><svg width="14" height="12" viewBox="0 0 14 12"><rect x="1" y="1" width="12" height="10" fill="none" stroke="#fff" stroke-width="1.5"/><path d="M1 1l6 5 6-5" fill="none" stroke="#fff" stroke-width="1.5"/></svg>info@harpervalept.com</div>
  <div class="btn btn-solid" style="left:870px;top:406px;width:135px;height:44px">Submit&nbsp;<svg width="14" height="12" viewBox="0 0 14 12"><path d="M1 6l12-5-4 11-2-5z" fill="#fff"/></svg></div>
  <div class="abs footer-rule"></div>
  <div class="abs copyright">© Copyright 2017. Harper Vale Personal Training. All rights reserved.</div>
  <div class="abs social footer-social"><span class="dot" style="background:#fff"></span><span class="dot" style="background:var(--orange)"></span><span class="dot" style="background:#fff"></span><span class="dot" style="background:#fff"></span></div>
</footer>

</body>
</html>
```